Game, Voice & Dedicated Server Company Needs a Business Card Design

We need a new business card design, centered around our new logo (PSD provided below).

Designs that we do like:
https://pixelmarsh.net/item/corporate-business-card/5382017?s_rank=43 (needs to be made more eye catching)

Our main areas of business are:
- Dedicated Servers
- Game Servers
- Voice Servers
- Mitigation Security Specialists

Industry/Entity Type

Business

Contact Information for Business Card

On the card: (and anything else you would suggest)
- Staff member name
- Staff member position in company
- Staff member phone number
- Staff member email
- Other / Staff member Skype
- Website link

Colors
9bcb3c
abd036

Requirements
Must have
• Design of Card:
• - Green (same green as the logo)
• - Business / Corporate design
• - Something a little different / abstract that shouts premium

```html
<!DOCTYPE html>
<html lang="en">
<head>
<meta charset="UTF-8">
<title>Vantacore Business Card</title>
<link href="https://fonts.googleapis.com/css2?family=Arimo:wght@400;700&display=swap" rel="stylesheet">
<style>
  :root {
    --stage: #1c1c1c;
    --lime: #abd036;
    --lime-deep: #9bcb3c;
    --charcoal: #2b2b2b;
    --charcoal-dark: #232323;
    --paper: #f3f3f3;
    --paper-shade: #e2e2e2;
    --ink-light: #ffffff;
    --ink-soft: #d8d8d8;
  }
  * { margin: 0; padding: 0; box-sizing: border-box; }
  html, body {
    width: 1200px; height: 800px; overflow: hidden;
    background: var(--stage);
    font-family: "Arimo", Arial, sans-serif;
  }
  .canvas { position: relative; width: 1200px; height: 800px; }

  .card {
    position: absolute; width: 520px; height: 300px;
    border-radius: 4px; overflow: hidden;
    box-shadow: 0 18px 40px rgba(0,0,0,.55);
  }

  /* Contact side */
  .card-contact { left: 610px; top: 90px; display: flex; }
  .contact-brand {
    position: relative; width: 54%; height: 100%;
    background: linear-gradient(135deg, var(--paper) 0%, var(--paper-shade) 100%);
    display: flex; align-items: center; justify-content: center;
  }
  .brand-arc { position: absolute; left: 0; top: 0; }
  .brand-lockup { display: flex; align-items: center; gap: 10px; }
  .brand-square { width: 22px; height: 22px; background: var(--lime-deep); }
  .brand-name {
    font-weight: 700; font-size: 34px; color: var(--lime-deep);
    letter-spacing: -0.5px;
  }
  .contact-details {
    width: 46%; height: 100%;
    background: var(--charcoal);
    padding: 26px 18px 0 22px;
    display: flex; flex-direction: column; gap: 11px;
  }
  .detail-row { display: flex; align-items: flex-start; gap: 12px; color: var(--ink-light); font-size: 13px; line-height: 1.15; }
  .detail-icon {
    flex: none; width: 22px; height: 22px; border-radius: 50%;
    border: 2px solid var(--lime); display: flex; align-items: center; justify-content: center;
  }
  .staff-name { font-weight: 700; font-size: 16px; }
  .staff-position { font-size: 12px; color: var(--ink-soft); }

  /* Brand side */
  .card-brand { left: 90px; top: 420px; background: var(--lime); }
  .brand-face {
    height: 78%; display: flex; align-items: center; justify-content: center;
  }
  .brand-face .brand-square { width: 28px; height: 28px; background: var(--ink-light); }
  .brand-face .brand-name { color: var(--ink-light); font-size: 46px; }
  .url-band {
    height: 22%;
    background: linear-gradient(90deg, var(--charcoal-dark), #4a4a4a 55%, var(--charcoal-dark));
    display: flex; align-items: center; justify-content: center;
    color: var(--ink-light); font-size: 18px; letter-spacing: 2px;
  }
</style>
</head>
<body>
<main class="canvas">

  <section class="card card-contact">
    <div class="contact-brand">
      <svg class="brand-arc" width="60" height="300" viewBox="0 0 60 300" aria-hidden="true">
        <path d="M0 0 H40 Q4 70 14 170 Q2 120 0 170 Z" fill="var(--lime)"/>
      </svg>
      <div class="brand-lockup">
        <span class="brand-square"></span>
        <span class="brand-name">VANTACORE</span>
      </div>
    </div>
    <div class="contact-details">
      <div class="detail-row">
        <span class="detail-icon">
          <svg width="12" height="12" viewBox="0 0 12 12"><circle cx="6" cy="4" r="2.5" fill="#fff"/><path d="M1 12 Q6 5 11 12 Z" fill="#fff"/></svg>
        </span>
        <div><div class="staff-name">Staff's Name</div><div class="staff-position">Staff's Position</div></div>
      </div>
      <div class="detail-row">
        <span class="detail-icon">
          <svg width="12" height="12" viewBox="0 0 12 12"><path d="M6 11 L2.5 5.5 A4 4 0 1 1 9.5 5.5 Z" fill="#fff"/><circle cx="6" cy="4.5" r="1.5" fill="var(--charcoal)"/></svg>
        </span>
        <div>Staff's Address<br>goes here</div>
      </div>
      <div class="detail-row">
        <span class="detail-icon">
          <svg width="12" height="12" viewBox="0 0 12 12"><path d="M2 1.5 L4.5 1 L5.5 4 L4 5 Q5 7.5 7 8 L8 6.5 L11 7.5 L10.5 10 Q4 11 2 1.5 Z" fill="#fff"/></svg>
        </span>
        <div>0123456789</div>
      </div>
      <div class="detail-row">
        <span class="detail-icon">
          <svg width="12" height="12" viewBox="0 0 12 12"><rect x="1" y="2.5" width="10" height="7" fill="none" stroke="#fff" stroke-width="1.3"/><path d="M1 2.5 L6 7 L11 2.5" fill="none" stroke="#fff" stroke-width="1.3"/></svg>
        </span>
        <div>staffname@vantacore.com</div>
      </div>
      <div class="detail-row">
        <span class="detail-icon">
          <svg width="12" height="12" viewBox="0 0 12 12"><circle cx="6" cy="6" r="4" fill="#fff"/></svg>
        </span>
        <div>Staff.Name</div>
      </div>
      <div class="detail-row">
        <span class="detail-icon">
          <svg width="12" height="12" viewBox="0 0 12 12" fill="none" stroke="#fff" stroke-width="1.1"><circle cx="6" cy="6" r="4.8"/><ellipse cx="6" cy="6" rx="2" ry="4.8"/><path d="M1.2 6 H10.8"/></svg>
        </span>
        <div>www.vantacore.com</div>
      </div>
    </div>
  </section>

  <section class="card card-brand">
    <div class="brand-face">
      <div class="brand-lockup">
        <span class="brand-square"></span>
        <span class="brand-name">VANTACORE</span>
      </div>
    </div>
    <div class="url-band">www.vantacore.com</div>
  </section>

</main>
</body>
</html>
```